Equity, Effectiveness and Efficiency in charitable food relief sector

I am undertaking my PhD in food policy in the charitable food relief sector, specifically investigating the factors (supply, demand and capacity) that affect the introduction of nutrition policy and in turn, affect the sector's ability to achieve equity, effectiveness and efficiency.

I need a graphic device that incorporates this central idea of Equity, Effectiveness and Efficiency, and how the factors of supply, demand and capacity interact. There are sub-factors within supply (1-6), demand (7-10) and capacity (11 - 15). All these details are shown in the attached figure (Basic figure_Eq Effec Effic and factors.jpg)

This figure (Basic figure_Eq Effec Effic and factors.jpg) contains all the information I need in a graphic but I need something that is more visually appealing, and that can link the ideas in a format other than a table. The final graphic will outline how the food relief sector balances the core objectives of equity, effectiveness and efficiency with the factors (and sub-factors) of supply, demand and capacity.

```html
<!DOCTYPE html>
<html lang="en">
<head>
<meta charset="utf-8">
<title>Equity, Effectiveness, Efficiency – Food Relief Factors</title>
<link href="https://fonts.googleapis.com/css2?family=Poppins:wght@500;600;700;800&display=swap" rel="stylesheet">
<style>
  :root {
    --title-red: #d93535;
    --title-red-light: #e94242;
    --supply: #9bbb1f;
    --demand: #22b3cb;
    --capacity: #ffa300;
    --teal: #408a8e;
    --pink: #ef5068;
    --sage: #8ba56c;
    --slate: #62779a;
    --line: #8c8c8c;
    --white: #ffffff;
  }
  * { margin: 0; padding: 0; box-sizing: border-box; }
  html, body { width: 1200px; height: 900px; overflow: hidden; }
  body {
    font-family: "Poppins", sans-serif;
    background: radial-gradient(ellipse at 50% 30%, #ffffff 0%, #f2f2f2 45%, #e2e2e2 100%);
    position: relative;
  }
  .connectors { position: absolute; inset: 0; width: 1200px; height: 900px; }
  .connectors path { stroke: var(--line); stroke-width: 1.5; fill: none; }

  .goal {
    position: absolute; left: 229px; top: 45px; width: 721px; height: 73px;
    border-radius: 37px;
    background: linear-gradient(180deg, var(--title-red-light), var(--title-red) 60%, #c42c2c);
    color: var(--white); font-weight: 800; font-size: 33px; letter-spacing: 0.5px;
    display: flex; align-items: center; justify-content: center;
    box-shadow: 0 14px 10px -10px rgba(0,0,0,.28);
  }
  .factor {
    position: absolute; width: 209px; height: 59px;
    border-radius: 0 4px 16px 0;
    color: var(--white); font-weight: 700; font-size: 17px; letter-spacing: 0.6px;
    display: flex; align-items: center; justify-content: center; gap: 10px;
    box-shadow: 0 12px 8px -9px rgba(0,0,0,.35);
  }
  .factor svg { width: 28px; height: 26px; fill: var(--white); }
  .factor--supply { left: 225px; top: 242px; background: var(--supply); }
  .factor--demand { left: 485px; top: 212px; background: var(--demand); }
  .factor--capacity { left: 743px; top: 242px; background: var(--capacity); }

  .sub {
    position: absolute; height: 50px; border-radius: 25px;
    color: var(--white); font-weight: 600; font-size: 13.5px; letter-spacing: 0.4px;
    display: flex; align-items: center; justify-content: center; white-space: nowrap;
    box-shadow: 0 10px 7px -8px rgba(0,0,0,.35);
  }
  .sub--supply { background: var(--teal); }
  .sub--demand { background: var(--pink); }
  .sub--capacity { background: var(--sage); }
  .sub--detail { background: var(--slate); }
</style>
</head>
<body>
  <svg class="connectors" viewBox="0 0 1200 900" aria-hidden="true">
    <path d="M590 118 V171 M331 171 H848"/>
    <path d="M331 171 V710 M277 349 H331 M277 494 H331 M277 638 H331"/>
    <path d="M590 171 V566 M562 349 H590 M562 494 H590"/>
    <path d="M848 171 V726 M847 349 H877 M1013 349 H1031 M848 422 H877"/>
    <path d="M944 494 H1031 M1016 494 V825"/>
  </svg>

  <div class="goal">EQUITY, EFFECTIVENESS, EFFICIENCY</div>

  <div class="factor factor--supply">
    <svg viewBox="0 0 28 26"><rect x="11" y="0" width="6" height="6"/><rect x="13" y="6" width="2" height="5"/><rect x="3" y="10" width="22" height="2"/><rect x="3" y="10" width="2" height="6"/><rect x="13" y="10" width="2" height="6"/><rect x="23" y="10" width="2" height="6"/><rect x="0" y="16" width="8" height="8"/><rect x="10" y="16" width="8" height="8"/><rect x="20" y="16" width="8" height="8"/></svg>
    SUPPLY
  </div>
  <div class="factor factor--demand">
    <svg viewBox="0 0 28 26"><rect x="1" y="11" width="6" height="14" rx="1"/><path d="M9 12 L14 4 C15 1 18 1 18 4 L17 10 H25 C27 10 28 12 27 14 L24 23 C23 25 22 25 20 25 H9 Z"/></svg>
    DEMAND
  </div>
  <div class="factor factor--capacity">
    <svg viewBox="0 0 28 26"><path d="M14 1 L21 4.5 V12 L14 15.5 L7 12 V4.5 Z M9 5.5 L14 8 L19 5.5 L14 3 Z M1 13 L7 10 L14 13.5 V21.5 L7 25 L0 21.5 V13.5 Z M3 14 L7 16 L11 14 L7 12 Z M14 13.5 L21 10 L28 13.5 V21.5 L21 25 L14 21.5 Z M17 14 L21 16 L25 14 L21 12 Z" fill-rule="evenodd"/></svg>
    CAPACITY
  </div>

  <div class="sub sub--supply" style="left:32px;top:325px;width:245px">Uncertain Material Supply</div>
  <div class="sub sub--supply" style="left:181px;top:397px;width:244px">Uncertain Material Supply</div>
  <div class="sub sub--supply" style="left:32px;top:469px;width:245px">Uncertain monetary supply</div>
  <div class="sub sub--supply" style="left:234px;top:541px;width:192px">Perishability</div>
  <div class="sub sub--supply" style="left:32px;top:613px;width:245px">Donor Constraints</div>
  <div class="sub sub--supply" style="left:234px;top:685px;width:192px">Donor Relationships</div>

  <div class="sub sub--demand" style="left:370px;top:325px;width:192px">Uncertain Demand</div>
  <div class="sub sub--demand" style="left:466px;top:397px;width:245px">Limited Demand Visibility</div>
  <div class="sub sub--demand" style="left:370px;top:469px;width:192px">Client Choice</div>
  <div class="sub sub--demand" style="left:494px;top:541px;width:192px">Food Wastage</div>

  <div class="sub sub--capacity" style="left:655px;top:325px;width:192px">Storage</div>
  <div class="sub sub--detail" style="left:877px;top:325px;width:136px">Cold</div>
  <div class="sub sub--detail" style="left:1031px;top:325px;width:136px">Warehouse</div>
  <div class="sub sub--capacity" style="left:877px;top:397px;width:192px">Transportation</div>
  <div class="sub sub--capacity" style="left:752px;top:469px;width:192px">Workforce</div>
  <div class="sub sub--detail" style="left:1031px;top:469px;width:136px">Volunteers</div>
  <div class="sub sub--detail" style="left:920px;top:533px;width:192px">Expertise &amp; Training</div>
  <div class="sub sub--capacity" style="left:752px;top:590px;width:192px">External Stakeholders</div>
  <div class="sub sub--detail" style="left:920px;top:645px;width:192px">Attitudes &amp; Beliefs</div>
  <div class="sub sub--capacity" style="left:752px;top:701px;width:192px">Budget</div>
  <div class="sub sub--detail" style="left:920px;top:758px;width:192px">Collaboration</div>
  <div class="sub sub--detail" style="left:920px;top:825px;width:192px">Executive Support</div>
</body>
</html>
```